Driftwood Bay Private Yacht Charter "Rack Flyer"

This will be a 4" x 9" Rack flyer that is 4 colors and two sided. This is a Private Yacht charter company that is based in St Thomas, U.S. Virgin Islands. Our main product that I would like to promote on one entire side of the flyer is our Private Luxury Full Day "Gilded Galley". our charter company is unique in the fact we offer customizable itineraries and we offer unique activities that keep the family and groups engaged in fun for the entire day. We would like something with our colors.

Target Market(s)

We are trying to reach an upscale clients that are looking for a Luxury Day Charter experience. these people will be most likely staying in Private Villas or staying at the Halloway Crest or PK Bellmont.

Requirements
Must have
• Contact Information:
Ph: (340) 555-0187
email: Info@driftwoodbayvoyages.example
www.driftwoodbayvoyages.example
One side should Promote our Gilded Galley (Gilded Galley is a trademarked name).
All Guests will receive "Harbor Fizz"
> Up to 12 guests
> Full Brunch Spread to include, Assorted fruit tower, Artesian Waffle Board, Frittata's, Loaded Avocado Toast or an All American Breakfast.
> Specialty Cocktails with Bottle Service options available
List all of our Unique activities to include:
Snorkeling
Underwater WaveGlider
Cliff Diving
Paddleboarding
Towable Activities
TEXT TO BE WRITTEN:
Experience yacht charter service at its Finest!
Sail away with us on a Luxury Charter experience complete with a full brunch spread. During our sail we will take you to the hottest destination spots in the Caribbean surrounding St Thomas and St John. Warm, fresh baked afternoon cookies will be served on the way back from our days journeys. Unlimited water, sodas, beer and rum punch will be provided for the entire group to enjoy throughout the day.
_________________

On side two of the brochure you can refer to the downloaded text. We do not want pricing listed on the flyer

```html
<!DOCTYPE html>
<html lang="en">
<head>
<meta charset="utf-8">
<title>Driftwood Bay Private Yacht Charter – Gilded Galley Rack Flyer</title>
<link href="https://fonts.googleapis.com/css2?family=Grandstander:wght@800;900&family=Lato:wght@400;700;900&family=Open+Sans:wght@800&display=swap" rel="stylesheet">
<style>
  :root{
    --sea:#1c63bf;
    --sea-deep:#0f3f92;
    --sea-light:#3d8fe0;
    --red:#e3232c;
    --white:#ffffff;
    --ink:#151515;
    --page:#eceef2;
  }
  *{box-sizing:border-box;margin:0;padding:0}
  html,body{width:1200px;height:1200px;overflow:hidden;background:var(--page)}
  .canvas{position:relative;width:1200px;height:1200px}
  .flyer{position:absolute;top:50px;width:458px;height:1100px;overflow:hidden;
    background:linear-gradient(180deg,var(--sea) 0%,#1a5cb8 50%,var(--sea-deep) 100%);
    box-shadow:0 6px 22px rgba(0,0,0,.18)}
  .flyer--front{left:130px}
  .flyer--back{left:612px;background:linear-gradient(180deg,#1b4fae 0%,#1d5cbd 55%,#1a55b4 100%)}
  .photo{position:absolute}
  .photo--round{border-radius:50%;border:4px solid var(--white);box-shadow:0 3px 10px rgba(0,0,0,.3)}

  /* front */
  .title{position:absolute;left:0;width:100%;text-align:center;color:var(--white);
    text-shadow:0 4px 0 #0d3a86,0 6px 14px rgba(0,0,0,.35)}
  .title__script{top:24px;font-family:"Grandstander",cursive;font-weight:900;font-size:90px;line-height:1;padding-left:20px}
  .title__block{top:128px;font-family:"Open Sans",sans-serif;font-weight:800;font-size:84px;line-height:1;padding-left:18px;letter-spacing:-1px}
  .photo--aerial{left:222px;top:270px;width:210px;height:150px;border-radius:14px;transform:rotate(32deg);
    background:linear-gradient(135deg,#eef3fa 0%,#c4d3e8 55%,#8ea9cf 100%);box-shadow:0 4px 14px rgba(0,0,0,.2)}
  .photo--snorkel{left:24px;top:240px;width:154px;height:154px;
    background:linear-gradient(160deg,#4fa9c0,#1c5d76 70%,#0f3c52)}
  .photo--drinks{left:306px;top:510px;width:136px;height:136px;
    background:linear-gradient(160deg,#f4efe8,#e7d6c3 60%,#c94a3c)}
  .photo--family{left:0;top:432px;width:440px;height:480px;border-radius:200px 200px 0 0;
    background:linear-gradient(180deg,#c79a78 0%,#e8c7ab 40%,#dfe8f2 70%,#9bb7d6 100%)}
  .wave{position:absolute;left:0;bottom:0;width:458px;height:280px}
  .brand{position:absolute;left:0;width:100%;top:960px;display:flex;align-items:center;justify-content:center;gap:12px}
  .brand__mark{width:26px;height:26px;border-radius:50%;background:var(--red);flex:none}
  .brand__name{font-family:"Lato",sans-serif;font-weight:900;font-size:26px;line-height:1.15;color:var(--red)}

  /* back */
  .lead{position:absolute;top:24px;left:0;width:100%;text-align:center;color:var(--white);
    font-family:"Lato",sans-serif;font-weight:900;font-size:18px}
  .intro{position:absolute;top:60px;left:22px;width:414px;color:var(--white);
    font-family:"Lato",sans-serif;font-size:14px;line-height:22.4px;text-align:justify;text-align-last:center}
  .rule{position:absolute;left:24px;width:410px;height:1.5px;background:var(--red)}
  .rule--top{top:228px}
  .rule--bottom{top:516px}
  .features{position:absolute;top:264px;left:22px;width:300px;list-style:none;color:var(--white);
    font-family:"Lato",sans-serif;font-weight:700;font-size:17px;line-height:23px}
  .features li{position:relative;padding-left:28px;margin-bottom:13px}
  .features svg{position:absolute;left:0;top:2px;width:18px;height:18px}
  .badge{position:absolute;left:249px;top:255px;width:180px;height:180px;border-radius:50%;
    background:var(--red);border:3px solid var(--white);text-align:center;color:var(--white);
    font-family:"Grandstander",cursive;font-weight:800;padding-top:36px}
  .badge__small{font-size:19px;line-height:22px}
  .badge__big{font-size:27px;line-height:30px;margin-top:6px;letter-spacing:.5px}
  .photo--glass{left:324px;top:414px;width:32px;height:100px;border-radius:3px;
    background:linear-gradient(180deg,#f8c14a 0%,#f2961e 60%,#fdf3e0 100%)}
  .section-title{position:absolute;top:538px;left:0;width:100%;text-align:center;color:var(--white);
    font-family:"Grandstander",cursive;font-weight:900;font-size:29px;letter-spacing:.5px}
  .activity{position:absolute;width:130px;text-align:center;color:var(--white);
    font-family:"Lato",sans-serif;font-weight:700;font-size:16px;line-height:20px}
  .activity .photo{position:relative;display:block;width:90px;height:90px;margin:0 auto 8px}
  .act--snorkel{left:23px;top:597px}
  .act--snorkel .photo{background:linear-gradient(160deg,#9cc8d3,#2e6c83)}
  .act--glider{left:163px;top:597px}
  .act--glider .photo{background:linear-gradient(160deg,#5b8db3,#0e2b47)}
  .act--cliff{left:304px;top:597px}
  .act--cliff .photo{background:linear-gradient(180deg,#bfe3f3,#3fa8d0 55%,#6b4a36)}
  .act--paddle{left:77px;top:741px}
  .act--paddle .photo{background:linear-gradient(180deg,#d8e4ea,#8aa7b5 60%,#4d6d7e)}
  .act--towable{left:250px;top:741px}
  .act--towable .photo{background:linear-gradient(180deg,#cfe3ec,#e9e3da 55%,#c8a77f)}
  .contact{position:absolute;left:56px;top:950px;list-style:none;font-family:"Lato",sans-serif;color:var(--ink)}
  .contact li{display:flex;align-items:center;gap:14px}
  .contact__icon{width:30px;height:30px;border-radius:50%;background:var(--red);display:flex;align-items:center;justify-content:center;flex:none}
  .contact__icon svg{width:16px;height:16px}
  .contact__phone{font-size:36px;font-weight:900;margin-bottom:8px}
  .contact__line{font-size:19px;font-weight:400;margin-bottom:10px}
</style>
</head>
<body>
<main class="canvas">

  <section class="flyer flyer--front">
    <div class="photo photo--aerial" role="img" aria-label="Aerial view of a white catamaran on blue water"></div>
    <div class="photo photo--family" role="img" aria-label="Smiling family of three giving thumbs up"></div>
    <div class="photo photo--round photo--snorkel" role="img" aria-label="Snorkeler underwater wearing a mask"></div>
    <div class="photo photo--round photo--drinks" role="img" aria-label="Couple toasting cocktails over a brunch table"></div>
    <h1 class="title title__script">Gilded</h1>
    <div class="title title__block">GALLEY</div>
    <svg class="wave" viewBox="0 0 458 280" preserveAspectRatio="none" aria-hidden="true">
      <path d="M0,40 C120,110 300,90 458,10 L458,280 L0,280 Z" fill="#ffffff"/>
      <path d="M0,18 C120,92 300,74 458,0 L458,14 C300,88 120,104 0,44 Z" fill="var(--red)"/>
      <path d="M150,88 C280,84 380,40 458,6 L458,18 C380,52 280,92 150,88 Z" fill="var(--sea-deep)"/>
    </svg>
    <div class="brand">
      <span class="brand__mark"></span>
      <span class="brand__name">Driftwood Bay<br>Private Yacht Charter</span>
    </div>
  </section>

  <section class="flyer flyer--back">
    <h2 class="lead">Experience yacht charter service at its Finest!</h2>
    <p class="intro">Sail away with us on a Luxury Charter experience complete with a full brunch spread. During our sail we will take you to the hottest destination spots in the Caribbean surrounding St Thomas and St John. Warm, fresh baked afternoon cookies will be served on the way back from our days journeys. Unlimited water, sodas, beer and rum punch will be provided for the entire group to enjoy throughout the day.</p>
    <div class="rule rule--top"></div>

    <ul class="features">
      <li><svg viewBox="0 0 18 18"><rect x="1" y="3" width="13" height="13" fill="none" stroke="#fff" stroke-width="1.4"/><path d="M4 9 L7.5 13 L16 1" fill="none" stroke="#fff" stroke-width="1.6"/></svg>Up to 12 guests</li>
      <li><svg viewBox="0 0 18 18"><rect x="1" y="3" width="13" height="13" fill="none" stroke="#fff" stroke-width="1.4"/><path d="M4 9 L7.5 13 L16 1" fill="none" stroke="#fff" stroke-width="1.6"/></svg>Specialty Cocktails<br>with Bottle Service<br>options available</li>
      <li><svg viewBox="0 0 18 18"><rect x="1" y="3" width="13" height="13" fill="none" stroke="#fff" stroke-width="1.4"/><path d="M4 9 L7.5 13 L16 1" fill="none" stroke="#fff" stroke-width="1.6"/></svg>Full Brunch Spread<br>to include, Assorted fruit<br>tower, Artesian Waffle<br>Board, Frittata's, Loaded Avocado<br>Toast or an All American Breakfast</li>
    </ul>

    <div class="badge">
      <div class="badge__small">All Guests<br>will receive</div>
      <div class="badge__big">HARBOR<br>FIZZ</div>
    </div>
    <div class="photo photo--glass" role="img" aria-label="Sparkling orange brunch cocktail in a flute glass"></div>
    <div class="rule rule--bottom"></div>

    <h2 class="section-title">OUR UNIQUE ACTIVITIES</h2>

    <div class="activity act--snorkel"><span class="photo photo--round" role="img" aria-label="Snorkeler swimming over the sea floor"></span>Snorkeling</div>
    <div class="activity act--glider"><span class="photo photo--round" role="img" aria-label="Diver with an underwater scooter"></span>Underwater<br>WaveGlider</div>
    <div class="activity act--cliff"><span class="photo photo--round" role="img" aria-label="Friends jumping from a rock into the sea"></span>Cliff Diving</div>
    <div class="activity act--paddle"><span class="photo photo--round" role="img" aria-label="Couple on paddle boards"></span>Paddle Boarding</div>
    <div class="activity act--towable"><span class="photo photo--round" role="img" aria-label="Child riding a towable board in the surf"></span>Towable Activities</div>

    <svg class="wave" viewBox="0 0 458 280" preserveAspectRatio="none" aria-hidden="true">
      <path d="M0,70 C120,140 300,120 458,40 L458,280 L0,280 Z" fill="#ffffff"/>
      <path d="M0,46 C120,122 300,104 458,28 L458,42 C300,118 120,134 0,72 Z" fill="var(--red)"/>
      <path d="M150,118 C280,114 380,70 458,36 L458,48 C380,82 280,122 150,118 Z" fill="var(--sea-deep)"/>
    </svg>

    <ul class="contact">
      <li class="contact__phone"><span class="contact__icon"><svg viewBox="0 0 16 16"><path d="M3 1.5 L5.5 1.5 L6.5 5 L5 6.3 C5.8 8 7.6 9.9 9.7 11 L11 9.5 L14.5 10.5 L14.5 13 C14.5 14 13.5 14.6 12.5 14.5 C6.8 13.8 2.2 9.2 1.5 3.5 C1.4 2.5 2 1.5 3 1.5 Z" fill="#fff"/></svg></span>(340) 555-0187</li>
      <li class="contact__line"><span class="contact__icon"><svg viewBox="0 0 16 16"><rect x="1.5" y="3.5" width="13" height="9" fill="none" stroke="#fff" stroke-width="1.4"/><path d="M1.5 3.5 L8 9 L14.5 3.5" fill="none" stroke="#fff" stroke-width="1.4"/></svg></span>Info@driftwoodbayvoyages.example</li>
      <li class="contact__line"><span class="contact__icon"><svg viewBox="0 0 16 16"><circle cx="8" cy="8" r="6.3" fill="none" stroke="#fff" stroke-width="1.3"/><ellipse cx="8" cy="8" rx="2.8" ry="6.3" fill="none" stroke="#fff" stroke-width="1.1"/><path d="M1.7 8 H14.3 M2.8 4.8 H13.2 M2.8 11.2 H13.2" stroke="#fff" stroke-width="1.1"/></svg></span>www.driftwoodbayvoyages.example</li>
    </ul>
  </section>

</main>
</body>
</html>
```